ROSE WINE LABEL

WE NEED A LABEL DESIGN FOR A NEW ROSE WINE MADE IN MEXICO. THIS IS A NEW WINARY THAT WANTS TO DO SOMETHING DIFFERENT FOR THE WINE INDUSTRY IN MEXICO, EXCELENT QUALITY OF WINE ACCESIBLE FOR EVERYONE. WINE CULTURE IN MEXICO IS NOT GOOD, WE WANT TO INNOVATE IN THE MARKET, BRING WINE TO YOUNG PEOPLE WITHOUT MAKING IT SEAM LIKE A "LUXURY" PRODUCT, LET THEM KNOW THAT YOU CAN DRINK WINE EVERYDAY EVERYTIME, SOMETHING EASY TO ANALYZE, DRINK AND UNDERSTAND, SOMETHING TO LET KNOW THE CONSUMERS ABOUT THE GOOD QUALITY OF WINE YOU CAN FIND IN MEXICO. I WANT TO SEE A DIFFERENT DESIGN. WE WANT TO KEEP WORKING WITH THE DESIGNER FOR THE REST OF THE LABELS, AROUND 6-7. THE NAME OF THE WINARY IS "VINOS DEL RIOCLARO" AND THE NAMES OF THE WINES ARE GOING TO HAVE THE "RIOCLARO" AND THE DIFFERENT FINE ARTS LIKE PAINTING, DANCE, LITERATURE, ETC.
THE BOTTLE OF THIS WINE IS GOING TO BE REGULAR SHAPE ALSO KNOWN AS BODEAUX, TRANSPARENT AND LIGHT GREEN ALSO KNOWN AS "GREEN CHAMPAGNE", SILVER & BLACK CAPSULE.

Requirements
Must have
• THE LABEL MUST HAVE THE NAME OF THE WINE "BAILE DE LA SOLANA" AND IN A SMALLER FONT "QUERÉTARO, MÉXICO"
Nice to have
• A COLORFUL AND MODERN DESIGN, I AM ATTACHING THE LOGO OF THE WINARY. IT IS NOT NECESARY TO ADD IT TO THE LABEL, BUT PERHAPS SOMEONE IS INTERESTED IN THE "VR" OF THE DESIGN FROM INSIDE THE SHELL.
Should not have
• THE DESIGN SHOULD BE ABLE TO FIT IN A REGULAR FORM, RECTANGULAR, SQUARE, OR CIRCLE, NO SPECIAL DIE CUTTING CAN BE MADE TO THE LABEL.

```html
<!DOCTYPE html>
<html lang="es">
<head>
<meta charset="utf-8">
<title>Baile de la Solana — Etiqueta Rosado</title>
<link rel="stylesheet" href="https://fonts.googleapis.com/css2?family=Roboto+Slab:wght@300;600&display=swap">
<style>
  :root {
    --paper: #f7f2ea;
    --ink-light: #ffffff;
    --ink-soft: rgba(255, 255, 255, 0.88);
    --vermilion: #e5432a;
    --scarlet: #d9352a;
    --lime-glow: #b7d77a;
    --amber: #e98a45;
    --navy: #2c3466;
    --maroon: #6e1418;
    --wine: #8a1d22;
  }

  * { margin: 0; padding: 0; box-sizing: border-box; }

  html, body {
    width: 1200px;
    height: 1000px;
    overflow: hidden;
    background: var(--paper);
  }

  .canvas {
    position: relative;
    width: 1200px;
    height: 1000px;
    background: var(--paper);
  }

  .wine-label {
    position: absolute;
    left: 280px;
    top: 168px;
    width: 640px;
    height: 664px;
    overflow: hidden;
    background:
      radial-gradient(ellipse 38% 32% at 42% 16%, var(--lime-glow) 0%, rgba(183, 215, 122, 0.7) 40%, rgba(183, 215, 122, 0) 100%),
      radial-gradient(ellipse 30% 30% at 90% 10%, var(--vermilion) 0%, rgba(229, 67, 42, 0) 100%),
      radial-gradient(ellipse 34% 30% at 62% 78%, var(--navy) 0%, rgba(44, 52, 102, 0.75) 40%, rgba(44, 52, 102, 0) 100%),
      radial-gradient(ellipse 40% 40% at 96% 96%, var(--maroon) 0%, rgba(110, 20, 24, 0) 100%),
      radial-gradient(ellipse 40% 36% at 30% 48%, var(--amber) 0%, rgba(233, 138, 69, 0) 100%),
      linear-gradient(125deg, var(--scarlet) 0%, var(--vermilion) 40%, var(--wine) 100%);
  }

  .wine-label__text {
    position: absolute;
    left: 0;
    top: 226px;
    width: 464px;
    text-align: center;
    font-family: "Roboto Slab", serif;
    color: var(--ink-light);
  }

  .wine-label__vintage {
    font-weight: 300;
    font-size: 21px;
    letter-spacing: 1.5px;
    color: var(--ink-soft);
  }

  .wine-label__name {
    margin-top: 14px;
    font-weight: 600;
    font-size: 34px;
    letter-spacing: 0.5px;
    line-height: 1;
  }

  .wine-label__origin {
    margin-top: 18px;
    font-weight: 300;
    font-size: 22px;
    letter-spacing: 2.5px;
    color: var(--ink-soft);
  }
</style>
</head>
<body>
  <main class="canvas">
    <section class="wine-label" aria-label="Etiqueta de vino rosado Baile de la Solana">
      <div class="wine-label__text">
        <p class="wine-label__vintage">2013</p>
        <h1 class="wine-label__name">BAILE DE LA SOLANA</h1>
        <p class="wine-label__origin">QUERÉTARO, MÉXICO</p>
      </div>
    </section>
  </main>
</body>
</html>
```